We need a flyer design to promote Pembury & Vance Landscaping and Lawn Maintenance.

The flyer needs to be have:-
1) A great head line ( When quality matters)
2) A really awesome offer ( no obligation free trial mow)
3) A sense of scarcity (Due to time restraints, we can only take limited number of free lawn jobs. This offer is only available to the first 20 callers)
4) A call to action (Call now to avoid disappointment)
5) Contact details (Pembury & Vance Landscaping and Lawn Maintenance 0472 586 307)

The layout of the entire flyer should come across to potential customers as

1) simple to understand what Pembury & Vance offer (not overcrowd with messages; the main aim is to communicate across our services.)

The list of services that Pembury & Vance provide will be:-

- Lawn Mowing - Pruning - Weeding
- Mulching - Edging - Hedging
- Trimming - Fertilising - Garden maintenance
- Weekly, fortnightly or monthly programs

Thank you.

```html
<!DOCTYPE html>
<html lang="en">
<head>
<meta charset="utf-8">
<title>Pembury &amp; Vance Landscaping Flyer</title>
<link rel="stylesheet" href="https://fonts.googleapis.com/css2?family=Cinzel:wght@400;600&family=Oswald:wght@400;500;600&family=Roboto:wght@400;500&display=swap">
<style>
  :root {
    --backdrop: #d6d6d6;
    --paper: #ffffff;
    --paper-shade: #e9e9e9;
    --ink: #222222;
    --leaf: #1f9a4c;
    --leaf-light: #3aa54a;
    --forest: #125c31;
    --forest-deep: #0d4f2a;
  }
  * { margin: 0; padding: 0; box-sizing: border-box; }
  html, body { width: 1200px; height: 795px; overflow: hidden; background: var(--backdrop); }
  .flyer {
    position: absolute; left: 355px; top: 72px; width: 490px; height: 650px;
    background: linear-gradient(160deg, var(--paper-shade) 0%, var(--paper) 45%);
    overflow: hidden; font-family: "Oswald", sans-serif;
    box-shadow: 0 6px 18px rgba(0,0,0,.18);
  }
  .art { position: absolute; left: 0; top: 0; width: 490px; height: 650px; }
  .brand { position: absolute; left: 38px; top: 26px; text-align: center; width: 236px; }
  .brand__name { font-family: "Cinzel", serif; font-weight: 600; font-size: 23px; color: var(--ink); white-space: nowrap; }
  .brand__trade { font-family: "Cinzel", serif; font-size: 14px; letter-spacing: .55em; color: var(--leaf-light); margin-top: 2px; padding-left: .55em; }
  .brand__tagline { font-family: "Cinzel", serif; font-size: 11.5px; color: var(--ink); margin-top: 3px; }
  .services { position: absolute; left: 36px; top: 104px; color: var(--forest); }
  .services__title { font-size: 22px; font-weight: 600; letter-spacing: .01em; margin-bottom: 6px; }
  .services__list { list-style: none; }
  .services__item { display: flex; align-items: center; gap: 7px; height: 24.6px; font-size: 15px; font-weight: 500; text-transform: uppercase; }
  .services__item svg { width: 12px; height: 12px; flex: none; }
  .band { position: absolute; color: #fff; display: flex; align-items: center; white-space: nowrap; }
  .band--headline { left: 0; top: 384px; width: 246px; height: 33px; background: var(--leaf); padding-left: 26px; font-size: 20px; font-weight: 500; clip-path: polygon(0 0, 100% 0, 94% 100%, 0 100%); }
  .band--offer { left: 0; top: 420px; width: 280px; height: 26px; background: var(--forest); padding-left: 26px; font-size: 16px; font-weight: 500; clip-path: polygon(0 0, 100% 0, 95% 100%, 0 100%); }
  .band--scarcity { display: block; left: 140px; top: 451px; width: 340px; height: 27px; background: var(--forest); padding: 5px 0 0 28px; font-family: "Roboto", sans-serif; font-size: 6.8px; font-weight: 500; line-height: 1.35; letter-spacing: .02em; text-transform: uppercase; clip-path: polygon(4% 0, 100% 0, 100% 100%, 0 100%); }
  .band--scarcity span { display: block; }
  .band--cta { left: 118px; top: 486px; width: 230px; height: 42px; background: var(--leaf); justify-content: center; font-size: 31px; font-weight: 600; clip-path: polygon(10% 0, 100% 0, 100% 100%, 0 100%); padding-left: 16px; }
  .band--urgency { left: 178px; top: 528px; width: 205px; height: 24px; background: var(--forest); justify-content: center; font-family: "Roboto", sans-serif; font-size: 15.5px; font-weight: 500; clip-path: polygon(0 0, 100% 0, 95% 100%, 4% 100%); }
  .band--phone { left: 140px; top: 571px; width: 126px; height: 21px; background: var(--forest); justify-content: center; font-family: "Roboto", sans-serif; font-size: 14px; font-weight: 500; letter-spacing: .1em; }
  .band--social { left: 318px; top: 584px; width: 128px; height: 17px; background: var(--forest-deep); gap: 5px; padding-left: 8px; font-family: "Roboto", sans-serif; font-size: 6px; }
  .social__mark { width: 9px; height: 9px; background: #ffffff; opacity: .85; flex: none; }
  .perk { position: absolute; left: 22px; color: var(--leaf); font-size: 12.5px; font-weight: 500; text-transform: uppercase; }
  .perk--special { top: 540px; }
  .perk--full { top: 556px; }
  .more-info { position: absolute; left: 146px; top: 561px; font-family: "Roboto", sans-serif; font-size: 6.5px; font-weight: 500; color: var(--forest); text-transform: uppercase; }
  .contact { position: absolute; top: 596px; display: flex; align-items: center; gap: 4px; font-family: "Roboto", sans-serif; font-size: 6.5px; color: var(--forest); white-space: nowrap; }
  .contact svg { width: 8px; height: 8px; }
  .contact--email { left: 142px; }
  .contact--address { left: 242px; }
</style>
</head>
<body>
<main class="flyer">
  <svg class="art" viewBox="0 0 490 650">
    <defs>
      <linearGradient id="grass" x1="0" y1="0" x2="0" y2="1">
        <stop offset="0" stop-color="#7db356"/><stop offset="1" stop-color="#3f7d2b"/>
      </linearGradient>
      <linearGradient id="mowerGrass" x1="0" y1="0" x2="1" y2="0">
        <stop offset="0" stop-color="#c9222d"/><stop offset=".45" stop-color="#b82a2c"/><stop offset=".6" stop-color="#4f8d2c"/><stop offset="1" stop-color="#3c7a25"/>
      </linearGradient>
      <linearGradient id="stripes" x1="0" y1="0" x2="1" y2="1">
        <stop offset="0" stop-color="#3f7a2c"/><stop offset="1" stop-color="#7fb84e"/>
      </linearGradient>
      <linearGradient id="footer" x1="0" y1="0" x2="1" y2="0">
        <stop offset="0" stop-color="#8fc596"/><stop offset="1" stop-color="#3f9158"/>
      </linearGradient>
    </defs>
    <path role="img" aria-label="Photo of freshly cut lawn grass" d="M300,178 C360,214 420,240 490,236 V388 C445,392 412,378 388,344 L300,260 Z" fill="#4f8e30" stroke="#fff" stroke-width="4"/>
    <path role="img" aria-label="Photo of a gardener pushing a red lawn mower across green grass" d="M292,8 H490 V232 C450,236 410,214 372,186 C340,164 310,150 292,146 Z" fill="url(#grass)" stroke="#fff" stroke-width="4"/>
    <circle role="img" aria-label="Close-up photo of a red lawn mower wheel on grass" cx="256" cy="246" r="88" fill="url(#mowerGrass)" stroke="#fff" stroke-width="5"/>
    <path role="img" aria-label="Photo of a striped mown lawn with garden hedges" d="M335,288 A72,72 0 0 1 407,360 C407,400 380,425 345,435 C310,445 280,445 263,458 C263,420 263,390 263,360 A72,72 0 0 1 335,288 Z" fill="url(#stripes)" stroke="#fff" stroke-width="5"/>
    <polygon points="402,504 440,504 434,514 396,514" fill="var(--leaf)"/>
    <polygon points="380,518 402,518 396,526 374,526" fill="var(--forest)"/>
    <polygon points="116,552 172,552 166,562 110,562" fill="var(--leaf)"/>
    <polygon points="130,576 140,571 140,592 126,592" fill="var(--leaf)"/>
    <polygon points="270,573 292,573 286,583 264,583" fill="var(--leaf)"/>
    <polygon points="448,584 470,584 464,600 442,600" fill="var(--leaf)"/>
    <polygon points="70,608 490,608 490,650 60,650" fill="url(#footer)"/>
  </svg>

  <header class="brand">
    <h1 class="brand__name">PEMBURY &amp; VANCE</h1>
    <p class="brand__trade">LANDSCAPING</p>
    <p class="brand__tagline">AND LAWN MAINTENANCE</p>
  </header>

  <section class="services">
    <h2 class="services__title">WE PROVIDE:</h2>
    <ul class="services__list">
      <li class="services__item"><svg viewBox="0 0 12 12"><rect x=".5" y="2.5" width="9" height="9" fill="none" stroke="currentColor"/><path d="M2.5 6.5l2.3 2.3L11 1.5" fill="none" stroke="currentColor" stroke-width="2"/></svg>Lawn Mowing</li>
      <li class="services__item"><svg viewBox="0 0 12 12"><rect x=".5" y="2.5" width="9" height="9" fill="none" stroke="currentColor"/><path d="M2.5 6.5l2.3 2.3L11 1.5" fill="none" stroke="currentColor" stroke-width="2"/></svg>Pruning</li>
      <li class="services__item"><svg viewBox="0 0 12 12"><rect x=".5" y="2.5" width="9" height="9" fill="none" stroke="currentColor"/><path d="M2.5 6.5l2.3 2.3L11 1.5" fill="none" stroke="currentColor" stroke-width="2"/></svg>Weeding</li>
      <li class="services__item"><svg viewBox="0 0 12 12"><rect x=".5" y="2.5" width="9" height="9" fill="none" stroke="currentColor"/><path d="M2.5 6.5l2.3 2.3L11 1.5" fill="none" stroke="currentColor" stroke-width="2"/></svg>Mulching</li>
      <li class="services__item"><svg viewBox="0 0 12 12"><rect x=".5" y="2.5" width="9" height="9" fill="none" stroke="currentColor"/><path d="M2.5 6.5l2.3 2.3L11 1.5" fill="none" stroke="currentColor" stroke-width="2"/></svg>Edging</li>
      <li class="services__item"><svg viewBox="0 0 12 12"><rect x=".5" y="2.5" width="9" height="9" fill="none" stroke="currentColor"/><path d="M2.5 6.5l2.3 2.3L11 1.5" fill="none" stroke="currentColor" stroke-width="2"/></svg>Hedging</li>
      <li class="services__item"><svg viewBox="0 0 12 12"><rect x=".5" y="2.5" width="9" height="9" fill="none" stroke="currentColor"/><path d="M2.5 6.5l2.3 2.3L11 1.5" fill="none" stroke="currentColor" stroke-width="2"/></svg>Trimming</li>
      <li class="services__item"><svg viewBox="0 0 12 12"><rect x=".5" y="2.5" width="9" height="9" fill="none" stroke="currentColor"/><path d="M2.5 6.5l2.3 2.3L11 1.5" fill="none" stroke="currentColor" stroke-width="2"/></svg>Fertilising</li>
      <li class="services__item"><svg viewBox="0 0 12 12"><rect x=".5" y="2.5" width="9" height="9" fill="none" stroke="currentColor"/><path d="M2.5 6.5l2.3 2.3L11 1.5" fill="none" stroke="currentColor" stroke-width="2"/></svg>Garden Maintenance</li>
    </ul>
  </section>

  <p class="band band--headline">WHEN QUALITY MATTERS</p>
  <p class="band band--offer">NO OBLIGATION FREE TRIAL MOW</p>
  <p class="band band--scarcity"><span>Due to time restraints, we can only take limited number of free lawn jobs.</span><span>This offer is only available to the first 20 callers!</span></p>
  <p class="band band--cta">CALL NOW!</p>
  <p class="band band--urgency">To avoid Disappointment</p>

  <p class="perk perk--special">Special Offer</p>
  <p class="perk perk--full">Full Service</p>

  <p class="more-info">Call us for more info</p>
  <p class="band band--phone">0472 586 307</p>

  <p class="contact contact--email"><svg viewBox="0 0 8 8"><rect x=".5" y="1.5" width="7" height="5" fill="none" stroke="currentColor"/><path d="M.5 1.5l3.5 3 3.5-3" fill="none" stroke="currentColor"/></svg>info@pemburyvance.com</p>
  <p class="contact contact--address"><svg viewBox="0 0 8 8"><path d="M4 7.8C2 5.2 1.2 4 1.2 2.9a2.8 2.8 0 0 1 5.6 0C6.8 4 6 5.2 4 7.8z" fill="currentColor"/><circle cx="4" cy="2.9" r="1" fill="#fff"/></svg>your addres goes here!</p>

  <div class="band band--social">
    <span class="social__mark"></span>/username
    <span class="social__mark"></span>/username
    <span class="social__mark"></span>/username
  </div>
</main>
</body>
</html>
```